Torvend Ledger Hub (Account) WP Design

We need an Account (Profile) Wordpress design to add to tlh.co.uk.

The design should be based on https://tlh.co.uk/about/. The look and feel of the menu on the left.

The logic, after login the header menu will add another page:

Before Login:
Home / About / Trading / Support /

After Login
Home / About / Trading / Support / Account (Demo) - Logout

When you click on the / Account /

"Account Profile" page is loaded where you can change the settings etc.

"Account Profile" menu on the left should look the same as in / About / (https://tlh.co.uk/about/)

We need the following sub-pages under "Account Profile"

- Profile
- Transfers
- Reports
- Security
- API Key
- Affiliates

Now looking into each page:
-
- Profile (Should be split into individual or business) a user can choose whether how he want to run his account:

[Individual]

Personal Details
First Name:
Middle Name:
Family Name:
Citizenship:
Gender:
DOB:

[Attach File] (Government Issues ID, Passport, Driving License) - Verify

Contact Information
Phone: +44 207 318 4426 - Verify
E-Mail: sample@mailverno.com - Verify

Residential Address
Address line 1:
Address line 2:
Address line 3:
City:
Postcode:
Country:

[Attach File] (Utility Bill or Bank Statement) - Verify

[Business]

Company Name:
Registration Number:

Registered Address
Address line 1:
Address line 2:
Address line 3:
City:
Postcode:
Country:

[Attach File] (Certificate of Incorporation) - Verify
[Attach File] (Memorandum & Articles of Association)
[Attach File] (Shareholder Register)

Company Contact Information
Website:

-

- Transfers (Where a user can link a bank account to deposit or withdraw funds from the account)

Transfers

Add a bank account:

Please select the country where beneficiary’s bank is domicile: [Please select]
Please select the currency you wish to make transfers in: [Please select]

Full beneficiary name:
Full beneficiary address:
Beneficiary bank name:
Beneficiary bank address:
Beneficiary Bank Identification Code (BIC)/Routing Code:
Beneficiary IBAN number/account number:

[SAVE]

Deposti funds to TLH Bank Account
Amount of currency to be received e.g. 2345.67 [Please select: USD, EUR, GBP] :
Full beneficiary name: Torvend Ledger Hub Limited
Full beneficiary address: Brenmoor Court
7-9 Kelvane Road
London, United Kingdom
Beneficiary bank name:
Beneficiary bank address:
Beneficiary Bank Identification Code (BIC)/Routing Code: XXXXXXXXXX
Beneficiary IBAN number/account number: XXXXXXXXXXXXXXXXXXXXXXXXXX

Deposit coins to TLH Coin Account
Amount of coins to be received e.g. 2345.67 [Please select: BTC, LTC]:
TLH Coin Account: XXXXXXXXXXXXXXXXXXXXXXXXXXXXX

Applicable charges (?):
[Clear] [Continue]

Withdraw funds from TLH Bank Account
Amount of currency to be sent e.g. 2345.67 [Please select: USD, EUR, GBP] :

Withdraw coins from TLH Coin Account:
Amount of coins to be sent e.g. 2345.67 [Please select: BTC, LTC]:
Please specify you coin account: XXXXXXXXXXXXXXXXXXXXXXXXXXXXX

Applicable charges (?):
[Clear] [Continue]

-

- Reports

TBC
-

- Security

Change Password
Current Password:
New Password:
Confirm New Password:

Enable / Disable : Two-factor Authentication (SMS)

-

- API Key
TBC

-
- Affiliates

Unlimited earning potential!
You'll receive up to 10% commission on all trades made through your affiliate link.

Partner Affiliate Network
Simply apply to our program from your publisher account or click the "Join Now" button below.

Quorvelle.com - Join Now

```html
<!DOCTYPE html>
<html lang="en">
<head>
<meta charset="utf-8">
<title>Torvend Ledger Hub – Account Profile</title>
<link href="https://fonts.googleapis.com/css2?family=Arimo:wght@400;700&display=swap" rel="stylesheet">
<style>
:root{
  --brand:#0099d4;
  --panel:#d0ebf6;
  --band-grey:#e4e4e4;
  --ink:#111;
  --muted:#666;
  --rule:#555;
  --field-border:#b9cfd9;
  --white:#fff;
  --btn-dark:#4a4a4a;
}
*{box-sizing:border-box;margin:0;padding:0}
html,body{width:1173px;height:1200px;overflow:hidden;background:var(--white)}
body{font-family:"Arimo",Arial,sans-serif;color:var(--ink)}
.page{position:relative;width:1200px;height:1228px;transform:scale(.9775);transform-origin:0 0}
.abs{position:absolute}

/* header */
.top-rule{left:0;top:0;width:1160px;height:1px;background:#bbb}
.brand{display:flex;align-items:center;gap:10px}
.brand-name{font-size:16px;font-weight:400;color:#333;white-space:nowrap}
.brand-dot{width:14px;height:14px;border-radius:50%;background:var(--brand)}
.main-nav{left:290px;top:68px;font-size:12px;color:var(--muted)}
.login{left:696px;top:41px;display:flex;gap:10px}
.login-field{width:130px;height:26px;border:1px solid #c8c8c8;border-radius:3px;font-size:12px;color:#999;padding:6px 5px;position:relative}
.login-field::after{content:"?";position:absolute;right:4px;top:3px;width:18px;height:18px;border:1px solid #bbb;border-radius:50%;font-size:11px;text-align:center;line-height:16px}
.btn{display:inline-block;color:var(--white);font-size:11px;border-radius:3px;text-align:center}
.btn-login{width:54px;height:24px;line-height:24px;background:var(--btn-dark)}
.btn-signup{width:55px;height:24px;line-height:24px;background:var(--brand);margin-left:-4px}

/* ticker */
.ticker{left:0;top:94px;width:1200px;height:49px;background:var(--brand);color:var(--white)}
.ticker-icon{left:240px;top:9px;width:31px;height:31px;border:2px solid var(--white);border-radius:50%}
.ticker-icon::after{content:"";position:absolute;left:5px;top:5px;width:17px;height:17px;border-radius:50%;background:var(--white)}
.stat{top:7px}
.stat-label{font-size:11px}
.stat-value{font-size:14px;margin-top:2px}
.stat-value small{font-size:10px}
.stat-sep{top:0;width:1px;height:49px;background:rgba(255,255,255,.45)}

/* title band */
.title-band{left:0;top:143px;width:1200px;height:79px;background:var(--band-grey);border-bottom:1px solid #bbb}
.page-title{left:125px;top:167px;font-size:30px;font-weight:700;letter-spacing:.3px}
.profile-tab{top:187px;font-size:12px;color:#222}

/* side nav */
.side-nav{left:123px;top:270px;width:221px;list-style:none}
.side-nav li{height:38px;border-bottom:1px solid var(--rule);font-size:14px;line-height:28px;padding-top:8px}
.side-nav li:first-child{height:33px;padding-top:3px;color:var(--brand);font-weight:700;font-size:15px}

/* panel */
.panel{left:393px;top:239px;width:785px;height:636px;background:var(--panel);border-radius:4px}
.section-title{font-size:12px;font-weight:700;color:var(--brand);letter-spacing:.3px}
.field-label{font-size:12px;color:#222}
.field{width:205px;height:33px;background:var(--white);border:1px solid var(--field-border);border-radius:5px;font-size:12px;font-weight:700;padding:10px 19px}
.verify{font-size:12px}
.verify b,.note b{text-decoration:underline}
.btn-attach{width:106px;height:31px;line-height:31px;background:var(--brand);color:var(--white);font-size:12px;text-align:center;border-radius:3px}
.note{font-size:12px}

/* footer */
.footer{left:0;top:898px;width:1200px;height:330px;background:var(--brand);color:var(--white)}
.footer .brand-name{color:var(--white)}
.footer .brand-dot{background:var(--white)}
.copyright{font-size:10px;line-height:14px}
.footer-heading{font-size:22px;font-weight:700}
.footer-links{list-style:none;font-size:12px;line-height:15px}
.social{display:flex;gap:12px}
.social span{width:28px;height:28px;border-radius:50%;background:var(--white)}
.tagline-art{left:515px;top:1105px;width:575px;height:80px;background:linear-gradient(90deg,rgba(255,255,255,.15),rgba(255,255,255,.3));border-radius:6px}
</style>
</head>
<body>
<div class="page">

  <div class="abs top-rule"></div>
  <div class="abs brand" style="left:113px;top:38px">
    <div class="brand-name">Torvend Ledger Hub</div>
    <div class="brand-dot"></div>
  </div>
  <div class="abs main-nav">Home · About · Trading · Support</div>
  <div class="abs login">
    <div class="login-field">Email</div>
    <div class="login-field">Password</div>
    <span class="btn btn-login">Log In</span>
    <span class="btn btn-signup">Sign Up</span>
  </div>

  <div class="abs ticker">
    <div class="abs ticker-icon" aria-hidden="true"></div>
    <div class="abs stat" style="left:284px"><div class="stat-label">Current Price</div><div class="stat-value">$444.13</div></div>
    <div class="abs stat-sep" style="left:372px"></div>
    <div class="abs stat" style="left:398px"><div class="stat-label">Daily Change</div><div class="stat-value">-9.54 <small>-2.10%</small></div></div>
    <div class="abs stat-sep" style="left:497px"></div>
    <div class="abs stat" style="left:523px"><div class="stat-label">Day's Range</div><div class="stat-value">$440.00 - $457.30</div></div>
    <div class="abs stat-sep" style="left:665px"></div>
    <div class="abs stat" style="left:691px"><div class="stat-label">Today's Open</div><div class="stat-value">$453.57</div></div>
    <div class="abs stat-sep" style="left:783px"></div>
    <div class="abs stat" style="left:809px"><div class="stat-label">24h Volume</div><div class="stat-value">7194 BTC</div></div>
  </div>

  <div class="abs title-band"></div>
  <h1 class="abs page-title">Account Profile</h1>
  <div class="abs profile-tab" style="left:899px">INDIVIDUAL</div>
  <div class="abs profile-tab" style="left:1020px">BUSINESS</div>

  <ul class="abs side-nav">
    <li>Profile</li><li>Transfers</li><li>Reports</li><li>Security</li><li>API Key</li><li>Affiliates</li>
  </ul>

  <div class="abs panel"></div>

  <div class="abs section-title" style="left:420px;top:268px">Personal Details</div>
  <div class="abs field-label" style="left:421px;top:319px">First Name:</div>
  <div class="abs field" style="left:523px;top:307px"></div>
  <div class="abs field-label" style="left:421px;top:364px">Middle Name:</div>
  <div class="abs field" style="left:523px;top:350px"></div>
  <div class="abs field-label" style="left:421px;top:409px">Family Name:</div>
  <div class="abs field" style="left:523px;top:393px"></div>
  <div class="abs field-label" style="left:421px;top:454px">Citizenship:</div>
  <div class="abs field" style="left:527px;top:437px"></div>
  <div class="abs field-label" style="left:421px;top:499px">Gender:</div>
  <div class="abs field" style="left:527px;top:480px"></div>
  <div class="abs field-label" style="left:421px;top:544px">DOB:</div>
  <div class="abs field" style="left:527px;top:523px"></div>
  <div class="abs btn-attach" style="left:418px;top:588px">Attach File</div>
  <div class="abs note" style="left:419px;top:641px">(Government Issues ID, Passport, Driving License) - <b>Verify</b></div>

  <div class="abs section-title" style="left:803px;top:268px">Contact Information</div>
  <div class="abs field-label" style="left:808px;top:319px">Phone:</div>
  <div class="abs field" style="left:868px;top:307px">+44 207 318 4426</div>
  <div class="abs verify" style="left:1088px;top:317px">- <b>Verify</b></div>
  <div class="abs field-label" style="left:808px;top:364px">E-Mail:</div>
  <div class="abs field" style="left:868px;top:350px">sample@mailverno.com</div>
  <div class="abs verify" style="left:1088px;top:360px">- <b>Verify</b></div>

  <div class="abs section-title" style="left:808px;top:432px">Residential Address</div>
  <div class="abs field-label" style="left:808px;top:487px">Address line 1:</div>
  <div class="abs field" style="left:916px;top:478px"></div>
  <div class="abs field-label" style="left:808px;top:532px">Address line 2:</div>
  <div class="abs field" style="left:916px;top:523px"></div>
  <div class="abs field-label" style="left:808px;top:577px">Address line 3:</div>
  <div class="abs field" style="left:916px;top:568px"></div>
  <div class="abs field-label" style="left:808px;top:622px">City:</div>
  <div class="abs field" style="left:916px;top:612px"></div>
  <div class="abs field-label" style="left:808px;top:667px">Postcode:</div>
  <div class="abs field" style="left:916px;top:657px"></div>
  <div class="abs field-label" style="left:808px;top:712px">Country:</div>
  <div class="abs field" style="left:916px;top:702px"></div>
  <div class="abs btn-attach" style="left:804px;top:765px">Attach File</div>
  <div class="abs note" style="left:812px;top:823px">Utility Bill or Bank Statement) - <b>Verify</b></div>

  <footer class="abs footer">
    <div class="abs brand" style="left:123px;top:50px">
      <div class="brand-name">Torvend Ledger Hub</div>
      <div class="brand-dot"></div>
    </div>
    <div class="abs copyright" style="left:123px;top:125px">© 2014 Torvend Ledger Hub.<br>All rights reserved</div>
    <div class="abs" style="left:463px;top:40px">
      <div class="footer-heading">ABOUT US</div>
      <ul class="footer-links" style="margin-top:14px">
        <li>Rulebook</li><li>Trading Fees</li><li>Partners</li><li>Security</li><li>Terms of Service</li><li>Privacy Policy</li><li>Latest News</li>
      </ul>
    </div>
    <div class="abs" style="left:719px;top:40px">
      <div class="footer-heading">SUPPORT</div>
      <ul class="footer-links" style="margin-top:14px">
        <li>What is Bitcoin?</li><li>How to buy a bitcoin?</li><li>How to sell a bitcoin?</li>
      </ul>
    </div>
    <div class="abs" style="left:949px;top:40px">
      <div class="footer-heading">FOLLOW TLH</div>
      <div class="social" style="margin-top:16px"><span></span><span></span><span></span><span></span></div>
    </div>
  </footer>
  <div class="abs tagline-art" role="img" aria-label="Hand-lettered tagline: Change the world one bitcoin at a time"></div>

</div>
</body>
</html>
```